Business Card Design job - Tessa's Business Cards

Simple elegant feminine design - Going out on my own as a Mortgage Broker.
My thoughts are the following details on the Front, middle of the card possibly? Phone and email smaller font than my name?
Tessa Marwick
Finance Specialist
p: 0438 217 905
e: tessa@marwickfinance.com.au
Bottom of the card
residential / commercial / equipment
I would like the Font in Rose Gold maybe white or black background? or Possibly a stone grey - are you able to do a few options? I'd like them embossed
Then I had an idea as a simple logo as per the attached if you get the idea in my scribble, my initials, capital T attached to a small m that leads/follows into a circle? Thicker Font In Rose Gold, middle of the card at the back.
Very open to ideas though and what colour you think would look better with the Rose Gold.
Thanks so much for your help, I am not very creative and savvy with this stuff :-)
Industry/Entity Type
Finance
Contact Information for Business Card
Tessa Marwick
p: 0438 217 905
Look and feel
Each slider illustrates characteristics of the customer's brand and the style your logo design should communicate.

```html
<!DOCTYPE html>
<html lang="en">
<head>
<meta charset="utf-8">
<title>Tessa Marwick – Business Cards</title>
<link href="https://fonts.googleapis.com/css2?family=Bitter:wght@800&family=Open+Sans:wght@400&display=swap" rel="stylesheet">
<style>
  :root {
    --backdrop: #c6d6df;
    --card: #3e3f41;
    --card-deep: #333436;
    --gold: #cfaa5f;
    --gold-light: #e2c58a;
    --rose: #d7a88c;
    --accent: #e0669a;
    --shadow: rgba(30, 40, 50, 0.25);
  }
  * { margin: 0; padding: 0; box-sizing: border-box; }
  html, body {
    width: 1200px; height: 1174px; overflow: hidden;
    background: var(--backdrop);
  }
  .sheet {
    position: relative; width: 1200px; height: 1174px;
    display: flex; flex-direction: column; align-items: center; justify-content: center; gap: 70px;
  }
  .card {
    position: relative; width: 640px; height: 366px;
    background: var(--card);
    box-shadow: 0 10px 28px var(--shadow);
    overflow: hidden;
  }

  /* Front: contact side */
  .front-pattern {
    position: absolute; left: 0; top: 0; width: 290px; height: 230px;
    background: linear-gradient(135deg, var(--gold-light) 0%, var(--gold) 35%, var(--card-deep) 100%);
    clip-path: polygon(0 0, 100% 0, 100% 35%, 45% 100%, 0 100%);
    opacity: 0.9;
  }
  .front-brand {
    position: absolute; left: 360px; top: 110px;
    display: flex; align-items: center; gap: 14px;
  }
  .brand-dot {
    width: 74px; height: 74px; border-radius: 50%;
    border: 2px solid var(--rose);
  }
  .brand-name {
    font-family: "Open Sans", sans-serif; font-weight: 400;
    color: var(--gold); font-size: 15px; letter-spacing: 2px; text-transform: uppercase;
  }
  .identity {
    position: absolute; left: 360px; top: 202px;
  }
  .identity-name {
    font-family: "Bitter", serif; font-weight: 800;
    color: var(--gold); font-size: 26px; letter-spacing: 0.5px;
  }
  .identity-title {
    font-family: "Open Sans", sans-serif; color: var(--rose);
    font-size: 13px; margin-top: 2px;
  }
  .contact {
    position: absolute; left: 40px; top: 238px; list-style: none;
    font-family: "Open Sans", sans-serif; color: var(--rose);
    font-size: 14px; letter-spacing: 0.6px; line-height: 32px;
  }
  .contact li { display: flex; align-items: center; gap: 10px; }
  .contact li::before {
    content: ""; width: 10px; height: 10px; border: 1.5px solid var(--accent);
  }
  .contact .services { text-transform: uppercase; }

  /* Back: brand side */
  .back-frame { position: absolute; inset: 0; }
  .back-brand {
    position: absolute; left: 90px; right: 0; top: 60px; bottom: 60px;
    display: flex; align-items: center; justify-content: center;
  }
  .back-mark {
    width: 176px; height: 176px; border-radius: 50%;
    border: 1.5px solid var(--rose);
    display: flex; align-items: center; justify-content: center; text-align: center;
  }
  .back-mark .brand-name { font-size: 16px; line-height: 1.5; }
</style>
</head>
<body>
<main class="sheet">

  <section class="card card-front">
    <div class="front-pattern" role="img" aria-label="Gold and charcoal leaf pattern"></div>
    <div class="front-brand">
      <span class="brand-dot"></span>
      <span class="brand-name">Marwick Finance</span>
    </div>
    <div class="identity">
      <p class="identity-name">Tessa Marwick</p>
      <p class="identity-title">Finance Specialiste</p>
    </div>
    <ul class="contact">
      <li>0438 217 905</li>
      <li>TESSA@MARWICKFINANCE.COM.AU</li>
      <li class="services">Residential / Commercial / Equipment</li>
    </ul>
  </section>

  <section class="card card-back">
    <svg class="back-frame" width="640" height="366" viewBox="0 0 640 366" role="img" aria-label="Gold leaf pattern border along the top, left and bottom edges">
      <defs>
        <linearGradient id="frameGold" x1="0" y1="0" x2="1" y2="0">
          <stop offset="0" stop-color="#e2c58a"/>
          <stop offset="0.5" stop-color="#cfaa5f"/>
          <stop offset="1" stop-color="#d7a88c"/>
        </linearGradient>
      </defs>
      <path d="M0 0 H640 V60 H90 V306 H640 V366 H0 Z" fill="url(#frameGold)"/>
    </svg>
    <div class="back-brand">
      <div class="back-mark">
        <span class="brand-name">Marwick<br>Finance</span>
      </div>
    </div>
  </section>

</main>
</body>
</html>
```